Hollow Lantern Distillery

I need a label designed for my small distillery. I’d like it to have a rose, and the name hollow lantern in script writing. I need the graphic to fit a standard gin bottle and I’ll need to be able to edit it depending on alcohol, warning and descriptions. I want it to look elegant and attractive, but slightly daring too. It’s a 700ml oslo bottle
Target Market(s)
Bespoke gin and vodka drinkers
Industry/Entity Type
Beverage
Font styles to use
Script
Other font styles liked:
- Something easy to read
Requirements
Must have
- Room for me to add and remove text depending on the drink
Nice to have
- Hollow lantern in script, slight colour on the rose and black writing

```html
<!DOCTYPE html>
<html lang="en">
<head>
<meta charset="utf-8">
<title>Hollow Lantern Gin Label</title>
<link rel="stylesheet" href="https://fonts.googleapis.com/css2?family=Rye&family=Playfair+Display:wght@700&display=swap">
<style>
  :root {
    --backdrop: #1a1a1a;
    --label-paper: #e7e7e7;
    --gold: #876838;
    --rose-red: #9b1f2a;
    --rose-soft: #b0404c;
    --ink: #050505;
  }
  html, body {
    margin: 0;
    padding: 0;
    width: 1200px;
    height: 1200px;
    overflow: hidden;
    background: var(--backdrop);
  }
  .label-canvas {
    display: block;
    width: 1200px;
    height: 1200px;
  }
  .label-paper { fill: var(--label-paper); }
  .gold-rule { fill: none; stroke: var(--gold); stroke-width: 7; }
  .name-band { fill: var(--gold); stroke: var(--ink); stroke-width: 2.5; }
  .band-inner-rule { fill: none; stroke: var(--rose-red); stroke-width: 5; }
  .band-ticks line { stroke: var(--rose-red); stroke-width: 25; stroke-dasharray: 7 7; }
  .rose-main { fill: var(--rose-red); }
  .rose-faded { fill: var(--rose-soft); }
  .product-name {
    font-family: "Rye", serif;
    font-size: 88px;
    fill: var(--ink);
    letter-spacing: 2px;
  }
  .spirit-type {
    font-family: "Playfair Display", serif;
    font-weight: 700;
    font-size: 48px;
    letter-spacing: 14px;
    fill: var(--ink);
  }
  .volume {
    font-family: "Playfair Display", serif;
    font-weight: 700;
    font-size: 21px;
    fill: var(--ink);
  }
</style>
</head>
<body>
<svg class="label-canvas" viewBox="0 0 1200 1200" xmlns="http://www.w3.org/2000/svg">
  <rect width="1200" height="1200" fill="var(--backdrop)"/>

  <!-- label body -->
  <path class="label-paper" d="M0 320 H160 L600 200 L1040 320 H1200 V880 H1040 L600 1000 L160 880 H0 Z"/>
  <path class="gold-rule" d="M0 338 H162 L600 218 L1038 338 H1200"/>
  <path class="gold-rule" d="M0 862 H162 L600 982 L1038 862 H1200"/>

  <!-- faded roses at the edges -->
  <g role="img" aria-label="Faded rose illustration at the left edge">
    <path class="rose-faded" d="M0 475 C20 470 30 450 48 455 C62 462 72 470 90 465 C100 478 92 500 108 508 C122 512 132 520 138 560 H0 Z"/>
  </g>
  <g role="img" aria-label="Faded rose illustration at the right edge">
    <path class="rose-faded" d="M1060 660 C1070 645 1090 640 1110 642 C1130 636 1150 640 1165 648 C1185 640 1200 645 1200 650 V728 C1180 730 1165 725 1150 720 C1135 732 1110 730 1095 720 C1075 715 1062 700 1060 680 Z"/>
  </g>

  <!-- name band -->
  <path class="name-band" d="M0 560 H158 L198 551 C220 492 270 446 350 446 C400 446 440 462 472 486 L1040 360 H1200 V640 H1040 L574 745 C552 815 500 862 420 862 C370 862 320 840 285 810 L162 838 H0 Z"/>
  <path class="band-inner-rule" d="M0 575 H160 L212 564 C232 506 282 460 350 460 C396 460 434 476 468 501 L1040 374 H1200"/>
  <path class="band-inner-rule" d="M0 823 H160 L290 794 C323 824 370 847 420 847 C492 847 542 805 562 731 L1040 625 H1200"/>
  <g class="band-ticks">
    <line x1="137" y1="585" x2="137" y2="815"/>
    <line x1="1062" y1="385" x2="1062" y2="615"/>
  </g>

  <!-- rose cluster above the band -->
  <g role="img" aria-label="Illustration of three red roses">
    <path class="rose-main" d="M487 320 C505 305 525 298 540 282 C555 268 565 258 585 262 C600 255 615 270 625 278 C640 272 655 262 650 290 C662 310 665 330 660 345 C680 338 700 340 712 350 C725 360 735 385 740 405 C748 430 735 460 715 470 C700 482 680 482 665 478 C650 490 625 495 600 480 C585 490 565 498 545 495 C520 500 495 488 482 470 C470 462 462 445 460 432 C455 420 470 408 470 400 C462 385 468 372 478 365 C482 355 475 340 487 320 Z"/>
  </g>

  <!-- product name -->
  <g transform="rotate(-12.8 600 600)">
    <text class="product-name" x="268" y="590">Hollow</text>
    <text class="product-name" x="360" y="690">Lantern</text>
  </g>

  <text class="spirit-type" x="607" y="916" text-anchor="middle">GIN</text>
  <text class="volume" x="1182" y="840" text-anchor="end">700 ml</text>
</svg>
</body>
</html>
```